Bref créative
Business cards/ Stationary for new travel agency
Stationary & business cards
Bright & Fun-filled
Marla & Ted Kinsolving
Moultrie, GA
marla@wanderpineharbortours.example
wanderpineharbortours.example

```html
<!DOCTYPE html>
<html lang="en">
<head>
<meta charset="utf-8">
<title>WanderPineHarbor Stationery</title>
<link href="https://fonts.googleapis.com/css2?family=Lato:wght@400;700&display=swap" rel="stylesheet">
<style>
  :root {
    --bg: #e4e5e6;
    --paper: #ffffff;
    --green: #5fa63a;
    --blue: #1d5fa8;
    --navy: #1b3e73;
    --ink: #4a5560;
    --faint: #eaf1f5;
  }
  html, body { margin: 0; padding: 0; overflow: hidden; }
  body {
    width: 1200px; height: 799px; background: var(--bg);
    font-family: "Lato", sans-serif; color: var(--ink); position: relative;
  }
  .letterhead, .card {
    position: absolute; background: var(--paper); overflow: hidden;
    box-shadow: 0 6px 18px rgba(0,0,0,0.18);
  }
  .letterhead { left: 90px; top: 55px; width: 480px; height: 690px; }
  .card { width: 420px; height: 240px; border-radius: 6px; left: 660px; }
  .card-front { top: 130px; }
  .card-back { top: 430px; }
  .swoosh { position: absolute; inset: 0; width: 100%; height: 100%; }
  .brand { position: absolute; display: flex; align-items: center; gap: 8px; }
  .brand-dot { width: 22px; height: 22px; border-radius: 50%; background: var(--blue); }
  .brand-name { font-weight: 700; font-size: 17px; color: var(--navy); letter-spacing: 0.3px; }
  .tagline { position: absolute; font-size: 8px; letter-spacing: 1.5px; text-transform: uppercase; color: var(--green); }
  .letterhead .brand { left: 36px; top: 46px; }
  .letterhead .tagline { left: 66px; top: 74px; }
  .watermark {
    position: absolute; left: 150px; top: 230px; width: 150px; height: 150px;
    border-radius: 50%; background: var(--faint);
  }
  .footer-contact {
    position: absolute; left: 36px; bottom: 34px; font-size: 8px; line-height: 1.6;
  }
  .card-front .brand { left: 22px; top: 28px; }
  .card-front .brand-name { font-size: 15px; }
  .card-front .tagline { left: 52px; top: 54px; font-size: 7px; }
  .holder { position: absolute; left: 190px; top: 28px; text-align: right; width: 130px; }
  .holder-name { font-size: 11px; font-weight: 700; color: var(--navy); }
  .holder-role { font-size: 8px; color: var(--green); margin-top: 2px; }
  .card-contact { position: absolute; left: 22px; top: 120px; font-size: 8px; line-height: 1.6; }
  .card-back .watermark { left: 140px; top: 50px; width: 120px; height: 120px; }
</style>
</head>
<body>
  <section class="letterhead">
    <svg class="swoosh" viewBox="0 0 480 690" preserveAspectRatio="none" aria-hidden="true">
      <path d="M480,180 C430,400 350,570 240,690 L290,690 C380,575 445,420 480,245 Z" fill="var(--green)"/>
      <path d="M480,262 C450,430 390,580 305,690 L480,690 Z" fill="var(--blue)"/>
    </svg>
    <div class="brand"><span class="brand-dot"></span><span class="brand-name">WanderPineHarbor</span></div>
    <div class="tagline">Travel &amp; Tours</div>
    <div class="watermark"></div>
    <div class="footer-contact">
      118 Harbor Lane<br>
      Moultrie, GA 31768<br>
      Tel 229-555-0142<br>
      Fax 229-555-0143<br>
      marla@wanderpineharbortours.example<br>
      wanderpineharbortours.example
    </div>
  </section>

  <section class="card card-front">
    <svg class="swoosh" viewBox="0 0 420 240" preserveAspectRatio="none" aria-hidden="true">
      <path d="M420,0 L372,0 C365,90 345,170 300,240 L335,240 C380,170 400,90 420,40 Z" fill="var(--green)"/>
      <path d="M420,60 C405,130 380,195 348,240 L420,240 Z" fill="var(--blue)"/>
    </svg>
    <div class="brand"><span class="brand-dot"></span><span class="brand-name">WanderPineHarbor</span></div>
    <div class="tagline">Travel &amp; Tours</div>
    <div class="holder">
      <div class="holder-name">Marla &amp; Ted Kinsolving</div>
      <div class="holder-role">Travel Consultants</div>
    </div>
    <div class="card-contact">
      118 Harbor Lane<br>
      Moultrie, GA 31768<br>
      Tel 229-555-0142<br>
      Fax 229-555-0143<br>
      marla@wanderpineharbortours.example<br>
      wanderpineharbortours.example
    </div>
  </section>

  <section class="card card-back">
    <svg class="swoosh" viewBox="0 0 420 240" preserveAspectRatio="none" aria-hidden="true">
      <path d="M420,150 C395,190 370,220 345,240 L420,240 Z" fill="var(--blue)"/>
    </svg>
    <div class="watermark"></div>
  </section>
</body>
</html>
```